Business Card for Jewelry Business

We need a new namecard design for a jewelry company based in Bangkok, Thailand. We have a new website recently and want the new namecard to reflect our new modern image. I have uploaded our old namecard to show you the information that needs to be on the namecard. Pls check our website www.qelnotrax.com for the new color scheme to help design the new namecard.

```html
<!DOCTYPE html>
<html lang="en">
<head>
<meta charset="utf-8">
<title>Qelnotrax Business Card</title>
<link href="https://fonts.googleapis.com/css2?family=Cinzel:wght@400&family=Arimo:wght@400&display=swap" rel="stylesheet">
<style>
  :root {
    --backdrop: #9c9c9c;
    --paper: #f6f6f4;
    --ink-dark: #2b2b2b;
    --ink-grey: #4a4a4a;
    --teal: #5cc8cd;
    --sand: #ddd6cc;
    --charcoal: #2e2e2e;
  }
  html, body {
    margin: 0;
    padding: 0;
    width: 1200px;
    height: 1050px;
    overflow: hidden;
    background: var(--backdrop);
  }
  .canvas {
    position: relative;
    width: 1200px;
    height: 1050px;
  }
  .card {
    position: absolute;
    top: 157px;
    width: 420px;
    height: 735px;
    box-sizing: border-box;
    border-bottom: 5px solid var(--teal);
  }
  .card--front {
    left: 120px;
    background: var(--paper);
    text-align: center;
    font-family: "Arimo", Arial, sans-serif;
    color: var(--ink-grey);
  }
  .card--back {
    left: 660px;
    background: var(--charcoal);
    display: flex;
    align-items: center;
    justify-content: center;
  }
  .brand {
    display: flex;
    align-items: center;
    justify-content: center;
    gap: 10px;
    font-family: "Arimo", Arial, sans-serif;
    color: var(--teal);
    letter-spacing: 4px;
  }
  .brand__dot {
    border-radius: 50%;
    background: var(--teal);
  }
  .card--front .brand {
    padding-top: 78px;
    font-size: 22px;
  }
  .card--front .brand__dot { width: 16px; height: 16px; }
  .card--back .brand { font-size: 34px; color: var(--sand); }
  .card--back .brand__dot { width: 24px; height: 24px; }
  .holder {
    margin: 70px 0 0;
    font-family: "Cinzel", "Times New Roman", serif;
    font-size: 30px;
    font-weight: 400;
    letter-spacing: 1px;
    color: var(--ink-dark);
  }
  .role {
    margin: 4px 0 0;
    font-size: 19px;
    color: var(--teal);
  }
  .divider {
    width: 52px;
    height: 1px;
    margin: 24px auto 24px;
    background: var(--ink-dark);
    border: 0;
  }
  .address {
    font-style: normal;
    font-size: 17px;
    line-height: 1.3;
  }
  .channels {
    display: flex;
    justify-content: center;
    gap: 8px;
    margin: 26px 0 22px;
    padding: 0;
    list-style: none;
  }
  .channels li {
    width: 22px;
    height: 22px;
    border-radius: 50%;
    background: var(--teal);
    display: flex;
    align-items: center;
    justify-content: center;
  }
  .contacts {
    font-size: 17px;
    line-height: 1.3;
  }
  .contacts p { margin: 0; }
</style>
</head>
<body>
<main class="canvas">
  <section class="card card--front">
    <div class="brand"><span class="brand__dot"></span>QELNOTRAX</div>
    <h1 class="holder">NARIN SOPHAKUL</h1>
    <p class="role">Sales&amp; Product Development Manager</p>
    <hr class="divider">
    <address class="address">
      218 Moo 7 Phetkasem Road<br>
      Trade Processing Zone 2<br>
      Sai Ngam Industrial Park<br>
      Sai Ngam, Bangkok 10930 Thailand
    </address>
    <ul class="channels">
      <li><svg width="12" height="12" viewBox="0 0 24 24"><path d="M6.6 10.8a15 15 0 0 0 6.6 6.6l2.2-2.2a1 1 0 0 1 1-.25 11 11 0 0 0 3.6.6 1 1 0 0 1 1 1V20a1 1 0 0 1-1 1A17 17 0 0 1 3 4a1 1 0 0 1 1-1h3.5a1 1 0 0 1 1 1 11 11 0 0 0 .6 3.6 1 1 0 0 1-.25 1z" fill="#fff"/></svg></li>
      <li><svg width="12" height="12" viewBox="0 0 24 24"><rect x="6" y="2" width="12" height="20" rx="2" fill="none" stroke="#fff" stroke-width="2.4"/></svg></li>
      <li><svg width="12" height="12" viewBox="0 0 24 24"><rect x="2" y="5" width="20" height="14" rx="1" fill="none" stroke="#fff" stroke-width="2.2"/><path d="M2 6l10 7 10-7" fill="none" stroke="#fff" stroke-width="2.2"/></svg></li>
      <li></li>
      <li></li>
      <li></li>
      <li></li>
    </ul>
    <div class="contacts">
      <p>+662-418-0275-9</p>
      <p>+662-850-3142</p>
      <p>studio@qelnotrax.com</p>
      <p>www.qelnotrax.com</p>
      <p>/Qelnotrax Makers</p>
      <p>@QelnotraxMkr</p>
      <p>QelnotraxMkr</p>
    </div>
  </section>

  <section class="card card--back">
    <div class="brand"><span class="brand__dot"></span>QELNOTRAX</div>
  </section>
</main>
</body>
</html>
```